TBW Construction
Stationary and Business Cards
Professional
Darek Venhollis
President
518 Marlow Ave
Westbrook, NJ 07099
tbwsonics@mailbox-example.com
tbwconstruction-example.com
NJ Lic# 58KT31720485
Commercial, Residential & Industrial

```html
<!DOCTYPE html>
<html lang="en">
<head>
<meta charset="utf-8">
<title>TBW Construction – Business Card</title>
<link href="https://fonts.googleapis.com/css2?family=Michroma&display=swap" rel="stylesheet">
<style>
  :root {
    --backdrop: #e4e2df;
    --card: #ffffff;
    --navy: #1f3f6b;
    --navy-deep: #173255;
    --ink: #2a2f36;
    --slate: #4d5560;
    --silver-light: #eceef0;
    --silver-dark: #9aa0a7;
  }
  * { margin: 0; padding: 0; box-sizing: border-box; }
  html, body { width: 1200px; height: 902px; overflow: hidden; }
  body {
    background: var(--backdrop);
    font-family: "Michroma", "Arial", sans-serif;
    color: var(--ink);
    position: relative;
  }
  .business-card {
    position: absolute;
    left: 100px; top: 165px;
    width: 1000px; height: 572px;
    background: var(--card);
    box-shadow: 0 14px 40px rgba(0,0,0,0.18);
    overflow: hidden;
  }
  .brand {
    position: absolute;
    top: 112px; left: 0; width: 100%;
    display: flex; justify-content: center; align-items: center; gap: 22px;
  }
  .brand-mark { width: 34px; height: 34px; background: var(--navy); }
  .brand-name {
    font-size: 44px; color: var(--navy); letter-spacing: 2px; text-transform: uppercase;
  }
  .holder {
    position: absolute; top: 272px; left: 0; width: 100%; text-align: center;
  }
  .holder-name { font-size: 20px; color: var(--navy); letter-spacing: 2px; }
  .holder-title { margin-top: 8px; font-size: 13px; color: var(--slate); letter-spacing: 3px; text-transform: uppercase; }
  .contacts {
    position: absolute; top: 374px; font-size: 13px; color: var(--ink); letter-spacing: 0.5px;
    white-space: nowrap;
  }
  .contacts li { list-style: none; display: flex; align-items: center; gap: 8px; height: 28px; }
  .contacts-left { left: 88px; }
  .contacts-right { left: 580px; }
  .contacts-left .phones span + svg { margin-left: 18px; }
  .icon { width: 16px; height: 16px; flex: none; }
  .footer-rail {
    position: absolute; top: 475px; height: 44px;
    background: linear-gradient(var(--silver-light), var(--silver-dark));
  }
  .rail-left { left: 0; width: 360px; }
  .rail-right { left: 950px; width: 50px; }
  .web-band {
    position: absolute; top: 466px; left: 340px; width: 615px; height: 62px;
    background: linear-gradient(var(--navy), var(--navy-deep));
    border-radius: 10px;
    color: #ffffff; font-size: 14px; letter-spacing: 5px;
    display: flex; align-items: center; justify-content: center;
    white-space: nowrap;
  }
</style>
</head>
<body>
  <section class="business-card">
    <header class="brand">
      <span class="brand-mark"></span>
      <span class="brand-name">TBW Construction</span>
    </header>

    <div class="holder">
      <p class="holder-name">Darek Venhollis</p>
      <p class="holder-title">President</p>
    </div>

    <ul class="contacts contacts-left">
      <li>
        <svg class="icon" viewBox="0 0 18 18"><circle cx="9" cy="9" r="9" fill="#2a2f36"/><path d="M9 4a3 3 0 0 0-3 3c0 2.3 3 6 3 6s3-3.7 3-6a3 3 0 0 0-3-3z" fill="#fff"/></svg>
        <span>518 Marlow Ave Westbrook, NJ 07099</span>
      </li>
      <li class="phones">
        <svg class="icon" viewBox="0 0 18 18"><circle cx="9" cy="9" r="9" fill="#2a2f36"/><path d="M6 5l2 2-1 1.2a6 6 0 0 0 2.8 2.8L11 10l2 2-1.3 1.3C8.5 13 5 9.5 4.7 6.3z" fill="#fff"/></svg>
        <span>973-555-0142</span>
        <svg class="icon" viewBox="0 0 18 18"><circle cx="9" cy="9" r="9" fill="#2a2f36"/><rect x="6.5" y="4" width="5" height="10" rx="1" fill="#fff"/></svg>
        <span>973-555-0187</span>
      </li>
    </ul>

    <ul class="contacts contacts-right">
      <li>
        <svg class="icon" viewBox="0 0 18 18"><circle cx="9" cy="9" r="9" fill="#2a2f36"/><circle cx="9" cy="9" r="4.5" fill="none" stroke="#fff" stroke-width="1.2"/><path d="M4.5 9h9M9 4.5v9" stroke="#fff" stroke-width="1"/></svg>
        <span>www.tbwconstruction-example.com</span>
      </li>
      <li>
        <svg class="icon" viewBox="0 0 18 18"><circle cx="9" cy="9" r="9" fill="#2a2f36"/><rect x="4.5" y="6" width="9" height="6.5" fill="#fff"/><path d="M4.5 6l4.5 3.5L13.5 6" fill="none" stroke="#2a2f36" stroke-width="1"/></svg>
        <span>tbwsonics@mailbox-example.com</span>
      </li>
    </ul>

    <div class="footer-rail rail-left"></div>
    <div class="footer-rail rail-right"></div>
    <div class="web-band">www.tbwconstruction-example.com</div>
  </section>
</body>
</html>
```